KelvoSHIELD Brochure

We need a new brochure designed for our KelvoSHIELD Unit. I have provided examples of previous and words for the new ones. Stock photos will be purchased and forwarded once design is complete.

I have also attached a competitors product brochure for reference. This is a bout conveying by using our product your people will be safe and will not need to use high rated PPE
Updates

Project Deadline Extended
Reason: Will be extending the project for 1 day and selecting the final design tomorrow to allow some of you to fine tune submissions.

Target Market(s)

Professionals

Industry/Entity Type

Product

Contact Information for Business Card

Refer Attached Details

Requirements
Must have
• Brantley Osgood Logo and Colours Business Card
• Brochure should complement KelvoSHIELD Logo

```html
<!DOCTYPE html>
<html lang="en">
<head>
<meta charset="utf-8">
<title>KelvoSHIELD Brochure</title>
<link href="https://fonts.googleapis.com/css2?family=Source+Sans+3:wght@300;400;600;700&display=swap" rel="stylesheet">
<style>
  :root {
    --backdrop: #d6d6d6;
    --paper: #f3f3f3;
    --brand-red: #c8133f;
    --brand-red-dark: #9a0e30;
    --stripe-grey: #444446;
    --navy: #1f4e79;
    --logo-blue: #1b6fae;
    --text-white: #ffffff;
    --tagline-grey: #e9e9e9;
  }
  * { margin: 0; padding: 0; box-sizing: border-box; }
  html, body {
    width: 1200px; height: 800px; overflow: hidden;
    background: var(--backdrop);
    font-family: "Source Sans 3", sans-serif;
  }
  .spread {
    position: absolute; left: 140px; top: 60px;
    width: 920px; height: 680px;
    background: var(--paper);
    box-shadow: 0 8px 24px rgba(0,0,0,0.18);
  }
  .spread-art { position: absolute; inset: 0; }
  .quote {
    position: absolute; left: 24px; top: 18px; width: 300px;
    color: var(--text-white); font-weight: 300; font-size: 13px;
    line-height: 1.4; text-transform: uppercase; letter-spacing: 0.2px;
  }
  .company-mark {
    position: absolute; left: 44px; top: 236px;
    display: flex; align-items: center; gap: 10px;
  }
  .company-mark .mark-square { width: 40px; height: 40px; background: var(--logo-blue); }
  .company-mark .mark-name { color: var(--navy); font-size: 17px; font-weight: 600; }
  .contact {
    position: absolute; left: 28px; top: 330px;
    color: var(--navy); font-size: 9.5px; line-height: 1.3;
  }
  .contact p { margin-bottom: 8px; }
  .contact b { font-weight: 700; }
  .contact .web { font-weight: 700; }
  .product-mark {
    position: absolute; left: 680px; top: 22px;
    color: var(--text-white); font-size: 30px; font-weight: 700;
  }
  .product-tagline {
    position: absolute; left: 622px; top: 76px;
    color: var(--tagline-grey); font-size: 11px; font-weight: 700;
    letter-spacing: 1.5px; text-transform: uppercase;
  }
  .headline {
    position: absolute; left: 487px; top: 240px;
    color: var(--navy); text-transform: uppercase; line-height: 1.25;
  }
  .headline .lead { display: block; font-size: 22px; font-weight: 700; }
  .headline .follow { display: block; font-size: 22px; font-weight: 400; }
</style>
</head>
<body>
  <main class="spread">
    <svg class="spread-art" width="920" height="680" viewBox="0 0 920 680">
      <defs>
        <linearGradient id="redBand" x1="0" x2="1" y1="0" y2="0">
          <stop offset="0" stop-color="#c8133f"/>
          <stop offset="0.5" stop-color="#c8133f"/>
          <stop offset="1" stop-color="#9a0e30"/>
        </linearGradient>
        <linearGradient id="photoLeft" x1="0" x2="1" y1="0" y2="1">
          <stop offset="0" stop-color="#e6e8ea"/>
          <stop offset="0.55" stop-color="#8c9fb8"/>
          <stop offset="1" stop-color="#27457e"/>
        </linearGradient>
        <linearGradient id="photoRight" x1="0" x2="1" y1="0" y2="1">
          <stop offset="0" stop-color="#5e6166"/>
          <stop offset="0.5" stop-color="#2c3140"/>
          <stop offset="1" stop-color="#1a1c24"/>
        </linearGradient>
      </defs>
      <polygon class="band-red" points="0,0 920,0 920,132 460,57 0,173" fill="url(#redBand)"/>
      <polygon class="band-grey" points="0,173 460,57 460,69 0,185" fill="#444446"/>
      <polygon class="band-grey" points="460,57 920,132 920,144 460,69" fill="#444446"/>
      <g role="img" aria-label="Photo of an electrician in a cap and safety glasses testing a switchboard with a multimeter">
        <polygon points="0,462 460,364 460,680 0,680" fill="url(#photoLeft)"/>
      </g>
      <g role="img" aria-label="Photo of a worker in arc flash face shield, hard hat and gloves operating electrical equipment">
        <polygon points="460,364 920,456 920,680 460,680" fill="url(#photoRight)"/>
      </g>
      <polygon class="band-red-thin" points="0,452 460,354 920,446 920,456 460,364 0,462" fill="#c8133f"/>
      <line x1="460" y1="0" x2="460" y2="680" stroke="rgba(0,0,0,0.08)" stroke-width="1"/>
    </svg>

    <p class="quote">"We take pride in our ability to successfully implement engineering projects so that they are executed thoroughly and reliably."</p>

    <div class="company-mark">
      <span class="mark-square"></span>
      <span class="mark-name">Brantley Osgood</span>
    </div>

    <div class="contact">
      <p>Level 20 (Northgate Building), 418 Ferris Street, Brisbane Australia 4000<br>PO Box 356 Albion QLD Australia 4010</p>
      <p><b>P</b> +61 7 3184 6290 &nbsp;<b>F</b> +61 7 3184 6200</p>
      <p><b>E</b> mark.ellery@BrantleyOsgood.com.au</p>
      <p class="web">www.BrantleyOsgood.com.au</p>
    </div>

    <div class="product-mark">KelvoSHIELD</div>
    <div class="product-tagline">KelvoSHIELD™ Arc Flash Mitigation</div>

    <h1 class="headline">
      <span class="lead">Protecting your people</span>
      <span class="follow">and your bottom line</span>
    </h1>
  </main>
</body>
</html>
```